Flyer design for mental health and disability support work company.

The company name 'Harbourlight Disability'

we need a flyer design for our company.

Specialising
Harbourlight Disability is a new KWPS service aimed towards KWPS participants with psychosocial/mental health, intellectual, and cognitive disabilities. We also specialise in supporting participants with a history of being involved in the criminal justice system.

Our focus
Focusing on providing core KWPS supports for community participation, daily activities and supported independent living.

Authentic
Like-minded people passionate about wanting to make a difference in participants' lives.

Our aim is to provide holistic and empowering support targeted towards creating independence and guidance for all participants and families.

Over 35 years of experience working with people with a vast range of disabilities and individual support needs.

Extensive experience not only within KWPS but working with mainstream services within NSW Fairway, Health, Corrections and Parole, Housing, Civic Desk NSW, Pathmark, Brief Assist, QTOB and NSW court systems.

website www.harbourlightdisability.com.au
email for referrals send to - referrals@harbourlightdisability.com.au
for further information send to - hello@harbourlightdisability.com.au

number 1800 372 519

Font styles to use
Serif

Requirements
Should not have
• pictures with people that have disabilities

```html
<!DOCTYPE html>
<html lang="en">
<head>
<meta charset="utf-8">
<title>Harbourlight Disability Flyer</title>
<link rel="stylesheet" href="https://fonts.googleapis.com/css2?family=Archivo+Black&family=Poppins:wght@700&family=Roboto+Slab:wght@600&family=Open+Sans:wght@400;700&display=swap">
<style>
  :root {
    --navy: #1c3160;
    --navy-deep: #142649;
    --orange: #f4a42a;
    --gold: #f7c25a;
    --ink: #2b3446;
    --paper: #ffffff;
    --backdrop: #e9ecf1;
  }
  * { box-sizing: border-box; margin: 0; padding: 0; }
  html, body { width: 1200px; height: 2400px; overflow: hidden; background: var(--backdrop); }
  .canvas { position: relative; width: 1200px; height: 2400px; }
  .flyer {
    position: absolute; left: 50px; top: 422px; width: 1100px; height: 1556px;
    background: var(--paper); overflow: hidden;
    font-family: "Open Sans", Arial, sans-serif; color: var(--ink);
    box-shadow: 0 10px 40px rgba(20, 38, 73, 0.18);
  }
  .flyer-shapes { position: absolute; inset: 0; }
  .brand-mark {
    position: absolute; left: 140px; top: 80px; width: 250px; height: 250px;
    border-radius: 50%; background: var(--navy);
    display: flex; align-items: center; justify-content: center; text-align: center;
    font-family: "Open Sans", Arial, sans-serif; font-weight: 700; font-size: 24px;
    color: var(--paper); line-height: 1.3; letter-spacing: 1px;
  }
  .title { position: absolute; left: 450px; top: 95px; width: 620px; white-space: nowrap; }
  .title-name {
    font-family: "Archivo Black", "Arial Black", sans-serif; font-size: 58px;
    color: var(--navy); line-height: 1.05; letter-spacing: 1px;
  }
  .title-sub {
    font-family: "Poppins", Arial, sans-serif; font-weight: 700; font-size: 72px;
    color: var(--orange); line-height: 1.15;
  }
  .section { position: absolute; width: 470px; }
  .section h2 {
    display: flex; align-items: center; gap: 16px;
    font-family: "Roboto Slab", Georgia, serif; font-weight: 600; font-size: 38px;
    color: var(--orange); margin-bottom: 8px; line-height: 1.2;
  }
  .section h2 svg { flex: none; }
  .section p { font-size: 20px; line-height: 1.3; margin-bottom: 12px; }
  .sec-specialising { left: 70px; top: 850px; }
  .sec-focus { left: 590px; top: 850px; }
  .sec-authentic { left: 70px; top: 1075px; }
  .sec-aim { left: 590px; top: 1025px; }
  .services-band {
    position: absolute; left: 60px; top: 1298px; width: 980px; height: 50px;
    background: var(--navy); color: var(--paper);
    font-weight: 700; font-size: 23px; display: flex; align-items: center; justify-content: center;
  }
  .contact { position: absolute; left: 70px; top: 1385px; color: var(--paper); }
  .contact h3 { font-size: 28px; font-weight: 700; margin-bottom: 6px; }
  .contact-row { display: flex; align-items: center; gap: 14px; font-size: 18px; margin-bottom: 4px; }
  .contact-row.phone { font-size: 30px; font-weight: 700; }
</style>
</head>
<body>
<div class="canvas">
  <div class="flyer">
    <svg class="flyer-shapes" viewBox="0 0 1100 1556" width="1100" height="1556">
      <defs>
        <linearGradient id="photoTone" x1="0" y1="0" x2="1" y2="1">
          <stop offset="0" stop-color="#f3ece6"/>
          <stop offset="0.5" stop-color="#d9b9a4"/>
          <stop offset="1" stop-color="#efe6df"/>
        </linearGradient>
        <radialGradient id="sunTone" cx="0.5" cy="1" r="1">
          <stop offset="0" stop-color="#f7c25a"/>
          <stop offset="1" stop-color="#f4a42a"/>
        </radialGradient>
      </defs>
      <path d="M0 0 H1100 V30 Q560 10 0 190 Z" fill="var(--navy)"/>
      <path d="M0 190 Q560 10 1100 30 V44 Q560 28 0 206 Z" fill="var(--orange)"/>
      <path d="M0 300 Q120 560 60 830 L0 830 Z" fill="var(--navy)"/>
      <path d="M0 330 Q90 560 30 830 L0 830 Z" fill="var(--orange)"/>
      <path d="M40 340 H1100 V760 Q620 850 40 800 Z" fill="url(#photoTone)" role="img" aria-label="Photo of two hands gently holding each other"/>
      <path d="M40 800 Q620 850 1100 760 V780 Q620 870 40 820 Z" fill="var(--paper)"/>
      <path d="M0 1372 Q520 1355 1100 1315 V1556 H0 Z" fill="var(--navy)"/>
      <path d="M560 1358 Q850 1340 1100 1290 V1318 Q830 1365 560 1374 Z" fill="var(--orange)"/>
      <path d="M780 1556 A140 140 0 0 1 1060 1556 Z" fill="url(#sunTone)" role="img" aria-label="Rising sun illustration"/>
    </svg>

    <div class="brand-mark">HARBOURLIGHT<br>DISABILITY</div>

    <div class="title">
      <div class="title-name">HARBOURLIGHT</div>
      <div class="title-sub">Disability</div>
    </div>

    <section class="section sec-specialising">
      <h2><svg width="36" height="36" viewBox="0 0 40 40"><circle cx="20" cy="20" r="16" fill="none" stroke="var(--orange)" stroke-width="4"/><circle cx="20" cy="20" r="6" fill="var(--orange)"/></svg>Specialising</h2>
      <p>Harbourlight Disability is a new KWPS service aimed toward KWPS participants with a history of criminal justice, psychosocial/ mental health, intellectual, and cognitive disabilities.</p>
    </section>

    <section class="section sec-focus">
      <h2><svg width="36" height="36" viewBox="0 0 40 40"><circle cx="20" cy="20" r="16" fill="none" stroke="var(--orange)" stroke-width="4"/><path d="M20 4 V12 M20 28 V36 M4 20 H12 M28 20 H36" stroke="var(--orange)" stroke-width="4"/></svg>Our focus</h2>
      <p>Focusing on providing core KWPS supports for community participation, daily activities and supported independent living.</p>
    </section>

    <section class="section sec-authentic">
      <h2><svg width="36" height="36" viewBox="0 0 40 40"><rect x="4" y="4" width="32" height="32" fill="none" stroke="var(--orange)" stroke-width="4"/><path d="M11 20 L18 27 L30 13" fill="none" stroke="var(--orange)" stroke-width="4"/></svg>Authentic</h2>
      <p>Likeminded people wanting to make a difference in participant's lives.</p>
      <p>Experience in working with mainstream supports under, Justice, Fairway Health, Corrections.</p>
    </section>

    <section class="section sec-aim">
      <h2><svg width="36" height="36" viewBox="0 0 40 40"><circle cx="20" cy="20" r="16" fill="none" stroke="var(--orange)" stroke-width="4"/><path d="M12 28 L28 12 M20 12 H28 V20" fill="none" stroke="var(--orange)" stroke-width="4"/></svg>Our aim</h2>
      <p>Our aim to provide holistic and empowering supports targeted towards creating independence and guidance for all participants and families.</p>
      <p>Over 35 years of experience working with people that have psychosocial, intellectual, and cognitive disabilities.</p>
    </section>

    <div class="services-band">Housing, Civic Desk NSW, Pathmark, Brief Assist and Court processes.</div>

    <div class="contact">
      <h3>Contact us :</h3>
      <div class="contact-row"><svg width="22" height="26" viewBox="0 0 22 26"><path d="M11 1 A9 9 0 0 1 20 10 C20 16 11 25 11 25 C11 25 2 16 2 10 A9 9 0 0 1 11 1 Z" fill="var(--paper)"/><circle cx="11" cy="10" r="3.5" fill="var(--navy)"/></svg>111 Street Name, city name, State name, country, 12345</div>
      <div class="contact-row phone"><svg width="26" height="26" viewBox="0 0 26 26"><path d="M6 2 L10 2 L12 8 L9 10 C10.5 13.5 12.5 15.5 16 17 L18 14 L24 16 L24 20 C24 22 22 24 20 24 C10 23 3 16 2 6 C2 4 4 2 6 2 Z" fill="var(--paper)"/></svg>123 456 789</div>
      <div class="contact-row"><svg width="24" height="24" viewBox="0 0 24 24"><circle cx="12" cy="12" r="10" fill="none" stroke="var(--paper)" stroke-width="2"/><path d="M2 12 H22 M12 2 C7 7 7 17 12 22 M12 2 C17 7 17 17 12 22" fill="none" stroke="var(--paper)" stroke-width="2"/></svg>www.harbourlightdisability.com</div>
    </div>
  </div>
</div>
</body>
</html>
```